ODE Sapphire Harbor Sell Sheet

We need a two-sided portrait-style sell sheet for a new insurance product called the ODE Sapphire Harbor. The ODE Sapphire Harbor is a custom Executive Risk commercial insurance policy that provides the broadest level of protection available in the marketplace. The sell sheet would primarily use the colors blue, gray and white, have clean lines, minimal graphics (perhaps a picture of an executive boardroom at the top), three boxes (or text areas) to provide a brief description of the specific insurance products provided by the Sapphire (Directors & Officers Liability, Employment Practices Liability, and Fiduciary Liability), be easy to read and really pique the reader's interest to learn more about the product. The title (ODE Sapphire Harbor) would overlay the graphic at the top, and just below the title would be the phrase "Expect More", which is our tagline for the product. There would be a two-sentence lead-in phrase just below the graphic ("Sapphire Harbor is an exclusive, custom-designed insurance policy tailored to a company’s specific risk profile. The policy was created to provide clients with a premium, industry-leading level of protection not found in the standard insurance marketplace". There needs to be another text section entitled "Return on Investment" and capable of containing three medium length sentences. There needs to be an "About Us" section (three to four medium-length sentences) and a "Contact Us" section (contact name, phone (x2), e-mail, address). On the back we want to discuss the specific features of the product by section of the policy (General Terms and Conditions, Directors & Officers Liability Insurance, Employment Practices Liability Insurance, Fiduciary Liability Insurance. This would likely be set out in bullet format.

I have attached a few examples found on the web that are similar to my vision for this sell sheet, but none that exactly fit our needs (whether graphically or due to specific layout).

Industry/Entity Type

Insurance

Font styles to use
Serif

Requirements
Must have
• I have uploaded a sample done in powerpoint. Please disregard the coloring as I did not have time to choose colors. I did not add the "About Us" and "Contact Us" sections on the front page and would like creative ideas on structuring that. On the back page, I think a nice looking table broken down by section of the policy would look nice, and allow us to enter bulleted coverage features for each section. Both graphics in the sample were found on google without watermarks by searching "board room" and "business agreement", respectively.

```html
<!DOCTYPE html>
<html lang="en">
<head>
<meta charset="utf-8">
<title>ODE Sapphire Harbor Sell Sheet</title>
<link href="https://fonts.googleapis.com/css2?family=Source+Sans+3:wght@400;600;700&display=swap" rel="stylesheet">
<style>
:root{
  --backdrop:#d4d5d7;
  --band:#ffffff;
  --blue:#1e9ad8;
  --ink:#3a3a3a;
  --charcoal:#2f2f30;
  --paper:#ffffff;
  --paper-soft:#f1f1f1;
  --photo-light:#d9d9d9;
  --photo-dark:#4a4a4a;
}
*{margin:0;padding:0;box-sizing:border-box}
html,body{width:1200px;height:854px;overflow:hidden}
body{background:var(--backdrop);font-family:"Source Sans 3",Arial,sans-serif;color:var(--ink);position:relative}
.top-band{position:absolute;left:0;top:0;width:1200px;height:42px;background:var(--band)}
.page{position:absolute;top:116px;width:489px;height:634px;background:var(--paper);box-shadow:3px 4px 8px rgba(0,0,0,.35);overflow:hidden}
.page--front{left:94px}
.page--back{left:637px}
.abs{position:absolute}

/* front */
.front-photo{left:0;top:0;width:489px;height:162px;background:linear-gradient(160deg,var(--photo-light) 0%,#9a9a9a 45%,var(--photo-dark) 100%)}
.title-block{left:0;top:162px;width:245px;height:58px;background:var(--charcoal);color:#fff;text-align:center;padding-top:6px;font-weight:400}
.title-block .name{font-size:11.5px;line-height:14px}
.title-block .tagline{display:flex;align-items:center;justify-content:center;gap:10px;font-size:11.5px;line-height:14px}
.title-block .tagline::before,.title-block .tagline::after{content:"";width:68px;height:1px;background:#fff}
.title-block .slogan{font-size:10.5px;line-height:15px}
.front-body{left:0;top:220px;width:245px;height:414px;background:var(--paper-soft)}
.copy{position:absolute;left:11px;width:222px;font-size:8px;line-height:10.4px;text-align:justify;color:#555}
.bar-head{position:absolute;left:0;width:218px;height:12px;background:var(--charcoal);color:#fff;font-size:8.6px;font-weight:600;line-height:12px;padding-left:11px}
.side-col{left:245px;top:144px;width:244px;height:409px;background:var(--blue);color:#fff}
.about-head{position:absolute;left:11px;top:24px;font-size:9px;font-weight:700}
.about-copy{position:absolute;left:11px;top:39px;width:222px;font-size:7.8px;line-height:10.4px;text-align:justify;font-weight:600}
.product{position:absolute;left:9px;width:230px}
.product-head{display:flex;align-items:center;gap:6px;font-size:7.6px;font-weight:700}
.product-head svg{width:37px;height:37px;flex:none}
.product ul{list-style:none;margin-top:5px;padding-left:4px}
.product li{font-size:7.8px;line-height:15.2px;font-weight:400}
.product li::before,.features li::before{content:"• ";font-size:6px}
.contact-col{left:245px;top:553px;width:244px;height:81px;background:var(--charcoal);color:#fff;padding:11px 0 0 13px}
.contact-row{display:flex;align-items:center;gap:8px;font-size:8.6px;height:22px}
.contact-row svg{width:16px;height:16px;flex:none}

/* back */
.back-photo{left:0;top:0;width:489px;height:210px;background:linear-gradient(200deg,#8a8a8a 0%,var(--photo-light) 55%,#b5b5b5 100%)}
.coverage-band{left:0;top:162px;width:489px;height:48px;background:rgba(30,154,216,.92);color:#fff;font-size:15px;font-weight:400;text-align:center;line-height:48px}
.col-head{position:absolute;height:30px;background:var(--charcoal);color:#fff;font-size:10.5px;font-weight:400;text-align:center;line-height:30px}
.features{position:absolute;list-style:none}
.features li{font-size:7.6px;line-height:15.2px;color:#444;white-space:nowrap}
.back-footer{left:0;top:586px;width:489px;height:48px;background:var(--charcoal);color:#fff}
.foot-item{position:absolute;top:15px;display:flex;align-items:center;gap:7px;font-size:8.6px}
.foot-item svg{width:17px;height:17px}
</style>
</head>
<body>
<div class="top-band"></div>

<section class="page page--front">
  <div class="abs front-photo" role="img" aria-label="Black and white photo of an executive boardroom table with leather chairs"></div>
  <div class="abs title-block">
    <div class="name">SAPPHIRE HARBOR</div>
    <div class="tagline">EXPECT MORE</div>
    <div class="slogan">“Industry-leading protection for Executive Risk.”</div>
  </div>
  <div class="abs front-body">
    <p class="copy" style="top:11px">Sapphire Harbor was created to address the market’s growing need for a premium Executive Risk insurance policy. Current solutions vary substantially in the coverage provided and limitations imposed. Despite an abundance of capacity, even recent new-to-market solutions contain trade-offs with respect to the policy’s terms and conditions. Insurance agents and buyers face challenging decisions often requiring meaningful sacrifices to coverage when selecting one policy over another. Sapphire Harbor is changing Executive Risk insurance by combining the industry’s most sought-after enhancements into a single, best-in-class solution.</p>
    <div class="bar-head" style="top:154px">RISK MANAGEMENT RETURN ON INVESTMENT</div>
    <p class="copy" style="top:168px">We view insurance premiums not as a cost of doing business, but rather as an investment in their risk management. A long-term approach is strongly recommended, rather than trying to ‘time the market’ with respect to the manifestation of a “Claim”. The policy’s language at the time of a “Claim” will determine the portion of loss covered by the policy. Therefore, breadth of coverage, rather than the cost of the policy (i.e. premium), is the recommended focal point to maximize risk management return on investment.</p>
    <div class="bar-head" style="top:282px">KNOW THE SCORE</div>
    <p class="copy" style="top:297px">Admittedly it can be difficult to compare two or more insurance proposals. In any comparison there are both objective and subjective factors to consider and weigh appropriately. Our Harbor Protection Index (“HPI”) helps to reduce those comparisons to two numbers: (i) an index score based on common terms and conditions of Executive Risk insurance policies, and (ii) a risk-specific score based on a particular client’s risk profile. HPI helps to ensure clients are getting the best protection to suit their specific insurance needs.</p>
  </div>

  <div class="abs side-col">
    <h2 class="about-head">ABOUT US</h2>
    <p class="about-copy">This is Photoshop’s version of Lorem Ipsum. Proin gravida nibh vel velit auctor aliquet. Aenean sollicitudin, lorem quis bibendum auctor, nisi elit consequat ipsum, nec sagittis sem nibh id elit. Duis sed odio sit amet nibh vulputate cursus a sit amet mauris. Morbi accumsan ipsum velit. Nam nec tellus a odio tincidunt auctor a ornare odio. Sed non mauris vitae erat consequat auctor eu in elit.</p>

    <div class="product" style="top:122px">
      <div class="product-head">
        <svg viewBox="0 0 37 37"><circle cx="18.5" cy="18.5" r="17" fill="none" stroke="#fff" stroke-width="1.6"/><circle cx="18.5" cy="18.5" r="13.5" fill="#fff" fill-opacity=".15"/><circle cx="18.5" cy="13" r="3.6" fill="#fff"/><path d="M11.5 25c0-4.5 3-7 7-7s7 2.5 7 7z" fill="#fff"/></svg>
        DIRECTORS &amp; OFFICERS LIABILITY INSURANCE
      </div>
      <ul><li>This is one line of text that will be used in the document</li><li>This is one line of text that will be used in the document</li><li>This is one line of text that will be used in the document</li></ul>
    </div>
    <div class="product" style="top:218px">
      <div class="product-head">
        <svg viewBox="0 0 37 37"><circle cx="18.5" cy="18.5" r="17" fill="none" stroke="#fff" stroke-width="1.6"/><circle cx="18.5" cy="18.5" r="13.5" fill="#fff" fill-opacity=".15"/><circle cx="13" cy="14.5" r="2.6" fill="#fff"/><circle cx="24" cy="14.5" r="2.6" fill="#fff"/><circle cx="18.5" cy="13" r="3" fill="#fff"/><path d="M8.5 24c0-3.2 2-5 4.5-5s4.5 1.8 4.5 5zM19.5 24c0-3.2 2-5 4.5-5s4.5 1.8 4.5 5zM13.5 25c0-3.8 2.2-6 5-6s5 2.2 5 6z" fill="#fff"/></svg>
        EMPLOYMENT PRACTICES LIABILITY INSURANCE
      </div>
      <ul><li>This is one line of text that will be used in the document</li><li>This is one line of text that will be used in the document</li><li>This is one line of text that will be used in the document</li></ul>
    </div>
    <div class="product" style="top:313px">
      <div class="product-head">
        <svg viewBox="0 0 37 37"><circle cx="18.5" cy="18.5" r="17" fill="none" stroke="#fff" stroke-width="1.6"/><circle cx="18.5" cy="18.5" r="13.5" fill="#fff" fill-opacity=".15"/><g stroke="#fff" stroke-width="1.2" fill="none"><path d="M18.5 9v16M14 26h9M11 12h15"/><path d="M11 12l-3 7h6zM26 12l-3 7h6z"/></g></svg>
        FIDUCIARY LIABILITY INSURANCE
      </div>
      <ul><li>This is one line of text that will be used in the document</li><li>This is one line of text that will be used in the document</li><li>This is one line of text that will be used in the document</li></ul>
    </div>
  </div>

  <div class="abs contact-col">
    <div class="contact-row"><svg viewBox="0 0 16 16"><circle cx="8" cy="8" r="7.5" fill="var(--blue)"/><circle cx="8" cy="8" r="5.5" fill="none" stroke="#fff" stroke-width=".8"/><path d="M6 4.8l1.2 1.6-.7.9c.4.9 1 1.5 1.9 1.9l.9-.7 1.6 1.2-.8 1.2c-2.6-.4-4.5-2.3-4.9-4.9z" fill="#fff"/></svg>000 000 0000</div>
    <div class="contact-row"><svg viewBox="0 0 16 16"><circle cx="8" cy="8" r="7.5" fill="var(--blue)"/><rect x="4" y="5.5" width="8" height="5.5" fill="#fff"/><path d="M4 5.5l4 3 4-3" fill="none" stroke="var(--blue)" stroke-width=".8"/></svg>odesapphire@harbormail.com</div>
    <div class="contact-row"><svg viewBox="0 0 16 16"><circle cx="8" cy="8" r="7.5" fill="var(--blue)"/><g fill="none" stroke="#fff" stroke-width=".8"><circle cx="8" cy="8" r="4.5"/><ellipse cx="8" cy="8" rx="2" ry="4.5"/><path d="M3.5 8h9M4.2 5.8h7.6M4.2 10.2h7.6"/></g></svg>www.odesapphire.com</div>
  </div>
</section>

<section class="page page--back">
  <div class="abs back-photo" role="img" aria-label="Black and white photo of a hand holding a pen over a business agreement"></div>
  <h1 class="abs coverage-band">COVERAGE HIGHLIGHTS</h1>

  <div class="col-head" style="left:6px;top:222px;width:153px">General Terms &amp; Conditions</div>
  <div class="col-head" style="left:167px;top:222px;width:155px">Directors &amp; Officers Liability</div>
  <div class="col-head" style="left:328px;top:222px;width:155px">Employment Practices Liability</div>
  <div class="col-head" style="left:328px;top:407px;width:155px">Fiduciary Liability</div>

  <ul class="features" style="left:9px;top:258px">
    <li>This is one line of text that will be used</li><li>This is one line of text that will be used</li><li>This is one line of text that will be used</li><li>This is one line of text that will be used</li><li>This is one line of text that will be used</li><li>This is one line of text that will be used</li><li>This is one line of text that will be used</li><li>This is one line of text that will be used</li><li>This is one line of text that will be used</li><li>This is one line of text that will be used</li><li>This is one line of text that will be used</li><li>This is one line of text that will be used</li><li>This is one line of text that will be used</li><li>This is one line of text that will be used</li><li>This is one line of text that will be used</li><li>This is one line of text that will be used</li><li>This is one line of text that will be used</li><li>This is one line of text that will be used</li><li>This is one line of text that will be used</li><li>This is one line of text that will be used</li>
  </ul>
  <ul class="features" style="left:171px;top:258px">
    <li>This is one line of text that will be used</li><li>This is one line of text that will be used</li><li>This is one line of text that will be used</li><li>This is one line of text that will be used</li><li>This is one line of text that will be used</li><li>This is one line of text that will be used</li><li>This is one line of text that will be used</li><li>This is one line of text that will be used</li><li>This is one line of text that will be used</li><li>This is one line of text that will be used</li><li>This is one line of text that will be used</li><li>This is one line of text that will be used</li><li>This is one line of text that will be used</li><li>This is one line of text that will be used</li><li>This is one line of text that will be used</li><li>This is one line of text that will be used</li><li>This is one line of text that will be used</li><li>This is one line of text that will be used</li><li>This is one line of text that will be used</li><li>This is one line of text that will be used</li>
  </ul>
  <ul class="features" style="left:332px;top:258px">
    <li>This is one line of text that will be used</li><li>This is one line of text that will be used</li><li>This is one line of text that will be used</li><li>This is one line of text that will be used</li><li>This is one line of text that will be used</li><li>This is one line of text that will be used</li><li>This is one line of text that will be used</li><li>This is one line of text that will be used</li><li>This is one line of text that will be used</li>
  </ul>
  <ul class="features" style="left:332px;top:441px">
    <li>This is one line of text that will be used</li><li>This is one line of text that will be used</li><li>This is one line of text that will be used</li><li>This is one line of text that will be used</li><li>This is one line of text that will be used</li><li>This is one line of text that will be used</li><li>This is one line of text that will be used</li><li>This is one line of text that will be used</li>
  </ul>

  <footer class="abs back-footer">
    <div class="foot-item" style="left:21px"><svg viewBox="0 0 16 16"><circle cx="8" cy="8" r="7.5" fill="var(--blue)"/><rect x="4" y="5.5" width="8" height="5.5" fill="#fff"/><path d="M4 5.5l4 3 4-3" fill="none" stroke="var(--blue)" stroke-width=".8"/></svg>odesapphire@harbormail.com</div>
    <div class="foot-item" style="left:205px"><svg viewBox="0 0 16 16"><circle cx="8" cy="8" r="7.5" fill="var(--blue)"/><circle cx="8" cy="8" r="5.5" fill="none" stroke="#fff" stroke-width=".8"/><path d="M6 4.8l1.2 1.6-.7.9c.4.9 1 1.5 1.9 1.9l.9-.7 1.6 1.2-.8 1.2c-2.6-.4-4.5-2.3-4.9-4.9z" fill="#fff"/></svg>000 000 0000</div>
    <div class="foot-item" style="left:345px"><svg viewBox="0 0 16 16"><circle cx="8" cy="8" r="7.5" fill="var(--blue)"/><g fill="none" stroke="#fff" stroke-width=".8"><circle cx="8" cy="8" r="4.5"/><ellipse cx="8" cy="8" rx="2" ry="4.5"/><path d="M3.5 8h9M4.2 5.8h7.6M4.2 10.2h7.6"/></g></svg>www.odesapphire.com</div>
  </footer>
</section>
</body>
</html>
```